I want a business letter head designed, one that I can have printed but also one that I can use as an insert for proforma documentation that is printed in house.

Business name : RJ Penfold & Associates
Address: PO Box 738
Tewantin Qld 4587

Type of business: Accounting practice- accounting, taxation, audit, self managed superannuation,

Colour scheme: black and blue - previously designed a business card; however the blue that is one the cards is very washed out and I am not particularly happy with it.

Industry/Entity Type

Business

```html
<!DOCTYPE html>
<html lang="en">
<head>
<meta charset="utf-8">
<title>RJ Penfold &amp; Associates — Letterhead</title>
<link rel="stylesheet" href="https://fonts.googleapis.com/css2?family=Source+Serif+4:wght@600&family=Open+Sans:wght@400&display=swap">
<style>
  :root {
    --backdrop: #e9e9e9;
    --paper: #f6f6f6;
    --ink-black: #0b0b0b;
    --brand-blue: #6b93c0;
    --watermark-blue: #d7dfea;
    --text-light: #ffffff;
  }
  * { box-sizing: border-box; margin: 0; padding: 0; }
  html, body {
    width: 1200px;
    height: 943px;
    overflow: hidden;
    background: var(--backdrop);
  }
  .letterhead {
    position: absolute;
    left: 289px;
    top: 31px;
    width: 622px;
    height: 880px;
    background: var(--paper);
    box-shadow: 0 2px 10px rgba(0,0,0,0.12);
    overflow: hidden;
  }
  .header-band {
    position: absolute;
    left: 0; top: 0;
    width: 100%;
    height: 92px;
    background: var(--ink-black);
    display: flex;
    align-items: center;
    padding-left: 150px;
    gap: 14px;
  }
  .brand-square {
    width: 34px;
    height: 34px;
    background: var(--brand-blue);
    flex: none;
  }
  .business-name {
    font-family: "Source Serif 4", Georgia, serif;
    font-weight: 600;
    font-size: 21px;
    line-height: 1.05;
    color: var(--text-light);
  }
  .header-rule {
    position: absolute;
    left: 0; top: 95px;
    width: 100%;
    height: 3px;
    background: var(--brand-blue);
  }
  .watermark-square {
    position: absolute;
    left: 300px;
    top: 300px;
    width: 300px;
    height: 300px;
    background: var(--watermark-blue);
  }
  .address-band {
    position: absolute;
    left: 0;
    bottom: 14px;
    width: 100%;
    height: 22px;
    display: flex;
    font-family: "Open Sans", Arial, sans-serif;
    font-size: 13px;
    line-height: 22px;
    color: var(--text-light);
  }
  .address-box {
    flex: 0 0 62%;
    background: var(--ink-black);
    text-align: right;
    padding-right: 8px;
  }
  .address-locality {
    flex: 1;
    background: var(--brand-blue);
    padding-left: 8px;
  }
</style>
</head>
<body>
  <main class="letterhead">
    <header class="header-band">
      <span class="brand-square"></span>
      <h1 class="business-name">RJ Penfold<br>&amp; Associates.</h1>
    </header>
    <div class="header-rule"></div>
    <div class="watermark-square"></div>
    <footer class="address-band">
      <span class="address-box">PO Box 738</span>
      <span class="address-locality">Tewantin Qld 4587</span>
    </footer>
  </main>
</body>
</html>
```